RM BIZ CARDS

Hi,

Is it possible to see a one sided version (with logo and info) as well as a two-sided version (front side w/logo and back side with info)?
How do we choose card stock and finish once we approve a design?

We would like the following info included:

Peter Lowell
Rosfeld Talent Media
4127 Marwick Lane, Suite 300
Los Angeles, CA 90041
(323) 555-0148
peter@rosfeldtalentmedia.example

```html
<!DOCTYPE html>
<html lang="en">
<head>
<meta charset="utf-8">
<title>Rosfeld Talent Media – Business Cards</title>
<link rel="stylesheet" href="https://fonts.googleapis.com/css2?family=Questrial&family=Cabin:wght@400;600&display=swap">
<style>
  :root {
    --page-bg: #e6e6e6;
    --card-dark: #141414;
    --card-dark-edge: #232323;
    --card-light: #f3f3f1;
    --ink: #1b1b1b;
    --ink-soft: #3a3a3a;
    --accent: #6b2a2a;
    --white: #ffffff;
  }
  * { margin: 0; padding: 0; box-sizing: border-box; }
  html, body { width: 1200px; height: 1000px; overflow: hidden; }
  body { background: var(--page-bg); position: relative; font-family: "Cabin", sans-serif; }

  .card {
    position: absolute;
    left: 250px;
    width: 693px;
    height: 414px;
  }
  .card--front {
    top: 58px;
    background: radial-gradient(ellipse at 50% 45%, var(--card-dark-edge), var(--card-dark) 75%);
  }
  .card--back {
    top: 500px;
    background: var(--card-light);
  }

  /* Front side */
  .front-brand {
    position: absolute;
    left: 0; right: 0;
    top: 150px;
    display: flex;
    flex-direction: column;
    align-items: center;
  }
  .front-brand__dot {
    width: 96px; height: 96px;
    border: 4px solid var(--white);
    border-radius: 50%;
    margin-bottom: 46px;
  }
  .front-brand__name {
    font-family: "Questrial", sans-serif;
    color: var(--white);
    font-size: 40px;
    letter-spacing: 4px;
    line-height: 1;
    white-space: nowrap;
  }

  /* Back side */
  .back-brand {
    position: absolute;
    left: 100px;
    width: 265px;
    top: 150px;
    display: flex;
    flex-direction: column;
    align-items: center;
  }
  .back-brand__dot {
    width: 62px; height: 62px;
    border: 3px solid var(--ink);
    border-radius: 50%;
    margin-bottom: 36px;
  }
  .back-brand__name {
    font-family: "Questrial", sans-serif;
    color: var(--ink);
    font-size: 24px;
    letter-spacing: 2px;
    line-height: 1;
    white-space: nowrap;
  }
  .divider {
    position: absolute;
    left: 363px;
    top: 135px;
    width: 2px;
    height: 152px;
    background: var(--ink-soft);
  }
  .contact {
    position: absolute;
    left: 382px;
    top: 132px;
    color: var(--ink-soft);
    font-size: 15px;
    line-height: 20px;
  }
  .contact__name {
    color: var(--accent);
    font-size: 21px;
    font-weight: 600;
    line-height: 26px;
    margin-bottom: 24px;
  }
  .contact__company {
    color: var(--ink);
    font-size: 17px;
    font-weight: 600;
    line-height: 22px;
  }
  .contact__line { display: flex; align-items: center; gap: 5px; }
  .contact__icon { width: 12px; height: 12px; flex: none; }
</style>
</head>
<body>

  <section class="card card--front" aria-label="Card front">
    <div class="front-brand">
      <div class="front-brand__dot" aria-hidden="true"></div>
      <div class="front-brand__name">ROSFELD TALENT</div>
    </div>
  </section>

  <section class="card card--back" aria-label="Card back">
    <div class="back-brand">
      <div class="back-brand__dot" aria-hidden="true"></div>
      <div class="back-brand__name">ROSFELD TALENT</div>
    </div>

    <div class="divider" aria-hidden="true"></div>

    <div class="contact">
      <div class="contact__name">Peter Lowell</div>
      <div class="contact__company">Rosfeld Talent Media</div>
      <div>4127 Marwick Lane, Suite 300</div>
      <div>Los Angeles, CA 90041</div>
      <div class="contact__line">
        <svg class="contact__icon" viewBox="0 0 24 24" aria-hidden="true">
          <path fill="var(--accent)" d="M6.6 10.8c1.4 2.8 3.8 5.1 6.6 6.6l2.2-2.2c.3-.3.7-.4 1-.2 1.1.4 2.3.6 3.6.6.6 0 1 .4 1 1V20c0 .6-.4 1-1 1C10.6 21 3 13.4 3 4c0-.6.4-1 1-1h3.5c.6 0 1 .4 1 1 0 1.3.2 2.5.6 3.6.1.3 0 .7-.2 1L6.6 10.8z"/>
        </svg>
        <span>(323) 555-0148</span>
      </div>
      <div class="contact__line">
        <svg class="contact__icon" viewBox="0 0 24 24" aria-hidden="true">
          <rect x="2" y="5" width="20" height="14" rx="1.5" fill="var(--accent)"/>
          <path d="M3 6.5l9 6.5 9-6.5" fill="none" stroke="var(--card-light)" stroke-width="1.6"/>
        </svg>
        <span>peter@rosfeldtalentmedia.example</span>
      </div>
    </div>
  </section>

</body>
</html>
```